Australian IT Company requires Business Card Design

Bluepeak is an Australian company that specialises in IT consulting & support, software development, project management, network services.

We have been in business for 15 years.

* We require a business card with the following on it:
Logo
Address
Contact Details
Space for staff name, title & mobile number

Industry/Entity Type

Software

```html
<!DOCTYPE html>
<html lang="en">
<head>
<meta charset="utf-8">
<title>Bluepeak Business Card</title>
<link rel="stylesheet" href="https://fonts.googleapis.com/css2?family=Montserrat:wght@600&family=Arimo:wght@400&display=swap">
<style>
  :root {
    --bg: #e9e6e2;
    --card-white: #ffffff;
    --brand-blue: #3d6a98;
    --brand-grey: #66686b;
    --name-grey: #d7dde4;
    --title-dark: #2b3a4a;
    --web-dark: #33516f;
  }
  html, body {
    margin: 0;
    width: 1200px;
    height: 900px;
    overflow: hidden;
    background: var(--bg);
  }
  .canvas {
    position: relative;
    width: 1200px;
    height: 900px;
  }
  .card {
    position: absolute;
    left: 100px;
    top: 172px;
    width: 1000px;
    height: 556px;
    background: var(--brand-blue);
    box-shadow: 0 10px 30px rgba(0,0,0,0.18);
    overflow: hidden;
    font-family: "Arimo", Arial, sans-serif;
  }
  .card__top {
    position: absolute;
    left: 0; top: 0;
    width: 100%;
    height: 250px;
    background: var(--card-white);
    border-bottom: 8px solid var(--brand-grey);
  }
  .brand {
    position: absolute;
    left: 70px;
    top: 92px;
    display: flex;
    align-items: center;
    gap: 26px;
  }
  .brand__square {
    width: 78px;
    height: 78px;
    background: var(--brand-blue);
  }
  .brand__name {
    font-family: "Montserrat", Arial, sans-serif;
    font-weight: 600;
    font-size: 64px;
    letter-spacing: 1px;
    line-height: 1;
    color: var(--brand-blue);
    text-transform: uppercase;
  }
  .brand__tagline {
    position: absolute;
    left: 176px;
    top: 182px;
    font-size: 15px;
    letter-spacing: 7px;
    color: var(--brand-grey);
    text-transform: uppercase;
  }
  .notch {
    position: absolute;
    left: 190px;
    top: 256px;
  }
  .contact {
    position: absolute;
    right: 60px;
    top: 290px;
    text-align: right;
    color: var(--card-white);
    font-size: 19px;
    line-height: 25px;
  }
  .contact__line { margin: 0; }
  .staff {
    position: absolute;
    left: 120px;
    top: 340px;
  }
  .staff__name {
    margin: 0;
    font-size: 40px;
    color: var(--name-grey);
    letter-spacing: 0.5px;
  }
  .staff__title {
    margin: 4px 0 0 80px;
    font-size: 28px;
    color: var(--title-dark);
  }
  .website {
    position: absolute;
    left: 0;
    right: 0;
    bottom: 50px;
    text-align: center;
    font-size: 24px;
    letter-spacing: 18px;
    color: var(--web-dark);
  }
</style>
</head>
<body>
<div class="canvas">
  <div class="card">
    <div class="card__top"></div>

    <div class="brand">
      <div class="brand__square"></div>
      <div class="brand__name">Bluepeak</div>
    </div>
    <div class="brand__tagline">Reliable IT For Growing Teams</div>

    <svg class="notch" width="70" height="40" viewBox="0 0 70 40" aria-hidden="true">
      <polygon points="4,2 66,2 35,36" fill="var(--brand-blue)" stroke="#ffffff" stroke-width="5" stroke-linejoin="miter"/>
    </svg>

    <div class="contact">
      <p class="contact__line">phone: +61 3 9555 0142</p>
      <p class="contact__line">email: contact@bluepeak.net.au</p>
      <p class="contact__line">address: 14 Ridge Street</p>
      <p class="contact__line">Level 3</p>
      <p class="contact__line">Carlton Vic 3053</p>
    </div>

    <div class="staff">
      <p class="staff__name">DANIEL REYES</p>
      <p class="staff__title">Director</p>
    </div>

    <div class="website">www.bluepeak.net.au</div>
  </div>
</div>
</body>
</html>
```